Coffee Cocktails Recipe Flips cards

create (12) recipe cards that illustrate the finished beverage, with its description, ingredients, and instructions. each card should be 5"x7" and styled to incorporate brand theme and the cultural elements of the beverage. cards will be used for stuffers in shipments of product, used by bartenders, and digitally shared. Present each drink in glassware that embodies the spirit of the culture it represents, garnishing with flair and a nod to the exotic origins, creating a multisensory experience that'll transport the drinker to distant lands with just one indulgent sip.
The presentation of each drink should reflect the cultural fusion aesthetically, using suggested glassware and garnishes to bring the exotic themes to life. Enjoy crafting these drinks and take your guests on a flavorful voyage around the world with each sip!

Target Market(s)

Consumers and Bars and Restaurants

Industry/Entity Type

coffee and adult beverages

Colors

Designer to choose colors to be used in the design.

Requirements
Must have
• brand alignment, styled to reflect the uniqueness of each recipe
Should not have
• appropriate glassware, garnishments, and images of raw ingredients

```html
<!DOCTYPE html>
<html lang="en">
<head>
<meta charset="utf-8">
<title>Café Mocha Bliss – Recipe Card</title>
<link href="https://fonts.googleapis.com/css2?family=Playfair+Display:ital,wght@1,700;1,800&family=Roboto:ital,wght@0,300;0,400;0,700;1,400;1,500&display=swap" rel="stylesheet">
<style>
  :root{
    --backdrop:#333333;
    --navy:#1c2e3a;
    --white:#ffffff;
    --ink:#1c2e3a;
    --mint:#1fe0a3;
    --rule:rgba(255,255,255,.35);
    --rule-dark:#1c2e3a;
  }
  *{margin:0;padding:0;box-sizing:border-box}
  html,body{width:1200px;height:879px;overflow:hidden;background:var(--backdrop)}
  body{position:relative;font-family:"Roboto",sans-serif}
  .card{position:absolute;top:20px;height:786px;overflow:hidden}
  .card--front{left:27px;width:561px;background:var(--navy);color:var(--white)}
  .card--back{left:610px;width:563px;background:var(--white);color:var(--ink)}

  .hero-photo{position:absolute;left:0;top:0;width:561px;height:440px;
    background:
      radial-gradient(ellipse 120px 190px at 265px 240px,#c08a55 0%,#8a5530 45%,transparent 75%),
      linear-gradient(90deg,#1a1c1e 0%,#3a3b3a 35%,#6b6a60 65%,#5f7a4e 100%);}
  .hero-photo::after{content:"";position:absolute;left:0;right:0;bottom:0;height:150px;
    background:linear-gradient(180deg,transparent,#d9d6d0 40%,#c9c4bc)}
  .wave{position:absolute;left:0;height:10px;
    background:radial-gradient(circle at 6px 0,transparent 5px,var(--wave) 5.6px) repeat-x;
    background-size:12px 10px}
  .card--front .wave{--wave:var(--navy);top:440px;width:561px}
  .card--back .wave{--wave:var(--white);top:406px;width:563px}

  .brand{position:absolute;left:31px;top:32px;display:flex;align-items:center;gap:8px}
  .brand__dot{width:52px;height:52px;border:2px solid var(--white);border-radius:50%}
  .brand__name{font-weight:700;font-size:21px;line-height:22px;letter-spacing:.3px;color:var(--white);width:90px}

  .title{position:absolute;left:0;width:561px;top:456px;text-align:center;
    font-family:"Playfair Display",serif;font-style:italic;font-weight:800;font-size:54px;line-height:62px}
  .blurb{position:absolute;left:29px;width:503px;top:530px;font-size:15.4px;line-height:18.5px;
    text-align:justify;text-align-last:center;font-weight:400}

  .stats{position:absolute;display:flex;border-top:1px solid var(--c);border-bottom:1px solid var(--c);height:47px}
  .stats__cell{display:flex;flex-direction:column;align-items:center;justify-content:center;border-right:1px solid var(--c)}
  .stats__cell:last-child{border-right:none}
  .stats__value{font-style:italic;font-size:16px;line-height:19px}
  .stats__value sup{font-size:8.5px}
  .stats__label{font-size:9.5px;margin-top:3px;white-space:nowrap}
  .card--front .stats{--c:var(--rule);left:33px;top:655px}
  .card--back .stats{--c:var(--rule-dark);left:32px;top:653px}

  .legal{position:absolute;left:35px;width:496px;font-size:10.4px;line-height:16px}
  .legal b{font-style:italic;font-weight:700}
  .card--front .legal{top:719px}
  .card--back .legal{top:718px;left:32px;width:500px}

  .links{position:absolute;left:0;width:100%;display:flex;justify-content:center;gap:12px;font-size:10.8px}
  .links span{display:flex;align-items:center;gap:4px}
  .links i{width:11px;height:11px;border:1.4px solid currentColor;border-radius:50%}
  .card--front .links{top:755px;left:-18px}
  .card--back .links{top:757px;left:28px}

  .ingredients-panel{position:absolute;left:0;top:0;width:563px;height:408px;background:var(--navy);color:var(--white)}
  .heading{position:absolute;left:32px;font-family:"Playfair Display",serif;font-style:italic;font-weight:700;font-size:31px;line-height:40px}
  .bar{position:absolute;left:32px;width:55px;height:6px;background:var(--mint)}
  .ingredients-panel .heading{top:30px}
  .ingredients-panel .bar{top:90px}
  .steps{position:absolute;left:32px;top:101px;width:270px;list-style:none}
  .steps li{display:flex;align-items:center;height:50px;border-bottom:1px solid var(--rule);font-size:14.8px;font-weight:300;white-space:nowrap}
  .steps li:last-child{border-bottom:none}
  .steps b{font-style:italic;font-weight:500;width:68px;flex:none}

  .arch{position:absolute;left:329px;top:31px;width:206px;height:428px;border-radius:103px 103px 0 0;
    border:3px solid var(--white);border-bottom:none;overflow:hidden}
  .arch__photo{position:absolute;inset:4px 4px 0 4px;border-radius:99px 99px 0 0;
    background:radial-gradient(ellipse 60px 80px at 50% 70%,#c7a17a 0%,#7a5a3f 50%,transparent 80%),
      linear-gradient(180deg,#2a2624 0%,#3b3431 60%,#4a3b30 100%)}

  .instructions .heading{top:426px}
  .instructions .bar{top:472px}
  .method{position:absolute;left:32px;top:484px;list-style:none;font-size:15.4px;line-height:23px;font-weight:400}
  .method li{display:flex}
  .method li span:first-child{font-style:italic;width:27px;flex:none}

  .seal{position:absolute;left:430px;top:604px;width:92px;height:92px;border:2px solid var(--navy);border-radius:50%;
    display:flex;align-items:center;justify-content:center;text-align:center;font-weight:700;font-size:14px;line-height:16px;color:var(--navy)}
</style>
</head>
<body>

<section class="card card--front">
  <div class="hero-photo" role="img" aria-label="Layered café mocha in a tall glass on a saucer with cocoa powder scattered on a marble counter"></div>
  <div class="wave"></div>
  <div class="brand"><span class="brand__dot"></span><span class="brand__name">RISE &amp; ROAST</span></div>

  <h1 class="title">Café Mocha Bliss</h1>
  <p class="blurb">Indulge in the balance of bittersweet espresso entwined with rich chocolate syrup to enjoy the luxe texture of the Café Mocha Bliss. Gently pour the espresso into your favorite mug, caress it with the velvety touch of chocolate, and crown the mix with steamed milk as soft as clouds. End with a swirl of whipped cream, graced with a sprinkling of chocolate shavings or a delicate dusting of cocoa powder—your canvas of comfort</p>

  <div class="stats">
    <div class="stats__cell" style="width:112px"><span class="stats__value">4.4g</span><span class="stats__label">Nootropics</span></div>
    <div class="stats__cell" style="width:114px"><span class="stats__value">770mg</span><span class="stats__label">Energy Boosters</span></div>
    <div class="stats__cell" style="width:96px"><span class="stats__value">300mg</span><span class="stats__label">Adaptogens</span></div>
    <div class="stats__cell" style="width:171px"><span class="stats__value">5mg<sup>THC</sup>&nbsp;&nbsp; 2mg<sup>CBD</sup></span><span class="stats__label">Full Spectrum Hemp Extract</span></div>
  </div>

  <p class="legal"><b>LEGAL:</b> This hemp product is federally legal with less than 0.3% Delta-9 THC by dry weight. Do not operate a vehicle or heavy machinery while under the influence of this product. Keep out of reach of children</p>

  <div class="links">
    <span><i></i>www.riseandroast.com</span>
    <span><i></i>rise&amp;roast</span>
    <span><i></i>riseroast</span>
  </div>
</section>

<section class="card card--back">
  <div class="ingredients-panel">
    <h2 class="heading">Ingredients:</h2>
    <div class="bar"></div>
    <ul class="steps">
      <li><b>Step-1</b>5g R&amp;R Classic Black Coffee</li>
      <li><b>Step-2</b>8oz hot water</li>
      <li><b>Step-3</b>2 tablespoons chocolate syrup</li>
      <li><b>Step-4</b>Steamed milk</li>
      <li><b>Step-5</b>Whipped cream</li>
      <li><b>Step-6</b>Chocolate shavings for garnish</li>
    </ul>
  </div>
  <div class="wave"></div>
  <div class="arch"><div class="arch__photo" role="img" aria-label="Foamy mocha in a clear glass mug on a saucer with coffee beans on a dark wooden table"></div></div>

  <div class="instructions">
    <h2 class="heading">Instructions:</h2>
    <div class="bar"></div>
    <ol class="method">
      <li><span>1-</span><span>Mix 8oz of hot water with one packet R&amp;R Classic Black<br>Instant Coffee mix well until powder is fully dissolved.</span></li>
      <li><span>2-</span><span>Pour the Coffee into a mug.</span></li>
      <li><span>3-</span><span>Stir in the chocolate syrup until well combined.</span></li>
      <li><span>4-</span><span>Top with steamed milk.</span></li>
      <li><span>5-</span><span>Add a generous dollop of whipped cream.</span></li>
      <li><span>6-</span><span>Garnish with chocolate shavings.</span></li>
    </ol>
  </div>

  <div class="stats">
    <div class="stats__cell" style="width:68px"><span class="stats__value">4.4g</span><span class="stats__label">Nootropics</span></div>
    <div class="stats__cell" style="width:76px"><span class="stats__value">770mg</span><span class="stats__label">Energy Boosters</span></div>
    <div class="stats__cell" style="width:84px"><span class="stats__value">300mg</span><span class="stats__label">Adaptogens</span></div>
    <div class="stats__cell" style="width:141px"><span class="stats__value">5mg<sup>THC</sup>&nbsp;&nbsp; 2mg<sup>CBD</sup></span><span class="stats__label">Full Spectrum Hemp Extract</span></div>
  </div>

  <div class="seal">RISE &amp;<br>ROAST</div>

  <p class="legal"><b>LEGAL:</b> This hemp product is federally legal with less than 0.3% Delta-9 THC by dry weight. Do not operate a vehicle or heavy machinery while under the influence of this product. Keep out of reach of children</p>

  <div class="links">
    <span><i></i>www.riseandroast.com</span>
    <span><i></i>rise&amp;roast</span>
    <span><i></i>riseroast</span>
  </div>
</section>

</body>
</html>
```